Need a revamp of our website to attract larger companies and government authorities. The site must breathe that we are a company ready for larger projects both in the web and app sector. And also, that we can start projects with short notice.

Until now the design suggestions for us have been mor suitable for smaller firms but we have now taken the step in the larger/bigger range.

Most of our web nowadays has been work on digitalization of all kinds of administrative systems.

The site to be redone is https://brightvanta.eu And that brand is a sub brand to https://farmount.se

startpage
servicelist presentation page
service detail page
caselist page (same as article list)
case detail page (same as article detail)
about us page
contact us page
Updates

We have this video that can be used as a hero banner video

https://www.filecrate.example/t/9QkLm2ZpRtWvXyNb

Target Market(s)

b2b customers

Coding

Coded - Design and coding required

Number of Pages Required

5+ page

Font styles to use
Sans Serif

Requirements
Must have
• A thought throu theme. with details folowing the whole design www.outcomera.se
Nice to have
• maybe a video hero banner https://www.filecrate.example/t/9QkLm2ZpRtWvXyNb
Should not have
• a standard theme look and feel.

```html
<!DOCTYPE html>
<html lang="en">
<head>
<meta charset="utf-8">
<title>Bright Vanta — Web &amp; Mobile Apps</title>
<link href="https://fonts.googleapis.com/css2?family=Open+Sans:wght@300;400;600;700&display=swap" rel="stylesheet">
<style>
:root{
  --blue:#1e9bef;
  --blue-dark:#0f7fd0;
  --navy:#0e2236;
  --ink:#2b2f36;
  --muted:#7a828c;
  --pale:#eef6fc;
  --line:#dfe6ec;
  --white:#ffffff;
}
*{box-sizing:border-box;margin:0;padding:0}
html,body{width:1200px;height:2660px;overflow:hidden}
body{font-family:"Open Sans",Arial,sans-serif;color:var(--ink);background:var(--white);position:relative}
.hero{position:absolute;left:0;top:0;width:1200px;height:620px;overflow:hidden}
.hero-photo{position:absolute;inset:0;background:linear-gradient(120deg,#5c6b58 0%,#8c9a8a 30%,#b9c2bd 55%,#6f7d6d 80%,#3f4a3d 100%)}
.hero-tint{position:absolute;inset:0;background:linear-gradient(180deg,rgba(14,34,54,.35),rgba(14,34,54,.55))}
.topbar{position:absolute;left:0;top:0;width:1200px;height:80px;display:flex;align-items:center;justify-content:space-between;padding:0 40px}
.brand{display:flex;align-items:center;gap:10px;color:var(--white);font-weight:700;font-size:18px;letter-spacing:.5px}
.brand-mark{width:30px;height:30px;border-radius:50%;background:var(--blue)}
.nav{display:flex;gap:26px;font-size:11px;font-weight:600;color:var(--white);letter-spacing:.5px}
.hero-copy{position:absolute;left:0;top:200px;width:1200px;text-align:center;color:var(--white)}
.hero-copy h1{font-weight:300;font-size:44px;line-height:48px;letter-spacing:1px}
.hero-copy h1 strong{font-weight:700;display:block}
.hero-copy p{width:560px;margin:22px auto 0;font-size:13px;line-height:20px;opacity:.9}
.hero-copy .call{margin-top:22px;font-size:17px;font-weight:600}
.btn{display:inline-block;background:var(--blue);color:var(--white);font-size:11px;font-weight:700;letter-spacing:.8px;padding:11px 24px}
.btn-outline{display:inline-block;border:1px solid var(--blue);color:var(--blue);font-size:11px;font-weight:700;letter-spacing:.8px;padding:10px 22px}
.hero-copy .btn{margin-top:40px;padding:13px 34px}

.apps{position:absolute;left:0;top:620px;width:1200px;height:340px;background:var(--pale)}
.apps-art{position:absolute;left:250px;top:50px;width:240px;height:240px;border-radius:6px;background:linear-gradient(160deg,#f6c94a 0%,#ea5a6f 35%,#5cc0ec 70%,#9a66d6 100%);opacity:.85}
.apps-copy{position:absolute;left:600px;top:80px;width:480px}
.apps-copy h2{font-weight:300;font-size:26px;color:var(--blue);line-height:32px;white-space:nowrap}
.apps-copy h2 strong{font-weight:700;color:var(--ink)}
.apps-copy p{margin-top:14px;width:420px;font-size:12px;line-height:19px;color:var(--muted)}
.apps-copy .actions{margin-top:24px;display:flex;gap:16px}

.section-title{font-weight:300;font-size:30px;color:var(--ink)}
.section-title strong{font-weight:700;color:var(--blue)}
.section-intro{margin-top:10px;width:520px;font-size:12px;line-height:19px;color:var(--muted)}

.services{position:absolute;left:80px;top:1000px;width:1040px}
.service-grid{margin-top:40px;display:grid;grid-template-columns:repeat(3,1fr);column-gap:60px;row-gap:44px}
.service{display:flex;gap:16px}
.service svg{flex:none}
.service h3{font-size:14px;font-weight:700;color:var(--ink)}
.service p{margin-top:6px;font-size:11.5px;line-height:18px;color:var(--muted)}

.clients{position:absolute;left:0;top:1460px;width:1200px;height:500px;background:var(--pale)}
.clients-inner{position:absolute;left:80px;top:40px;width:1040px}
.view-all{position:absolute;right:0;top:16px;font-size:11px;font-weight:700;color:var(--blue);letter-spacing:.5px}
.client-grid{margin-top:40px;display:grid;grid-template-columns:repeat(3,1fr);gap:40px}
.client-card{background:var(--white);height:320px;padding:36px 34px;text-align:center;box-shadow:0 2px 8px rgba(14,34,54,.06)}
.client-name{display:flex;align-items:center;justify-content:center;gap:10px;height:60px;font-size:20px;font-weight:700;color:var(--ink)}
.client-dot{width:22px;height:22px;border-radius:50%;background:var(--blue)}
.client-card p{margin-top:24px;font-size:12px;line-height:19px;color:var(--muted)}
.client-link{margin-top:24px;font-size:12px;font-weight:700;color:var(--blue)}
.client-sub{margin-top:4px;font-size:11px;color:var(--muted)}

.quote{position:absolute;left:0;top:1960px;width:1200px;height:410px}
.quote-copy{position:absolute;left:130px;top:90px;width:360px}
.quote-copy h2{font-weight:300;font-size:24px;color:var(--blue);line-height:30px}
.quote-copy h2 strong{font-weight:700;color:var(--ink);display:block;font-size:30px;line-height:38px}
.quote-copy p{margin-top:16px;font-size:12px;line-height:19px;color:var(--muted)}
.quote-copy .btn{margin-top:28px}
.devices-art{position:absolute;left:600px;top:40px;width:420px;height:330px;border-radius:6px;background:linear-gradient(180deg,#e4eaef 0%,#c4ced8 60%,#9aa8b5 100%)}

.footer{position:absolute;left:0;top:2370px;width:1200px;height:290px;background:var(--navy)}
.footer-panel{position:absolute;left:80px;top:20px;width:1040px;height:270px;background:var(--blue);display:grid;grid-template-columns:230px 300px 220px 1fr;gap:30px;padding:40px 40px;color:var(--white)}
.footer-brand{display:flex;flex-direction:column;align-items:center;justify-content:center;gap:12px;font-weight:700;font-size:18px;letter-spacing:.5px}
.footer-brand .brand-mark{width:54px;height:54px;background:var(--white)}
.footer h4{font-size:12px;font-weight:700;letter-spacing:.5px;margin-bottom:14px}
.field{height:26px;background:rgba(255,255,255,.9);margin-bottom:10px}
.btn-dark{background:var(--navy)}
.footer .small{font-size:11px;line-height:20px;opacity:.9}
.contact-row{display:flex;align-items:center;gap:10px;font-size:11px;margin-bottom:10px}
.socials{display:flex;gap:8px;margin-top:10px}
.socials span{width:20px;height:20px;border-radius:50%;background:rgba(255,255,255,.85)}
</style>
</head>
<body>

<header class="hero">
  <div class="hero-photo" role="img" aria-label="Photo of people gathered at an outdoor workshop table, soft natural tones"></div>
  <div class="hero-tint"></div>
  <div class="topbar">
    <div class="brand"><span class="brand-mark"></span>BRIGHT VANTA</div>
    <nav class="nav"><span>SERVICES</span><span>PROJECTS</span><span>ABOUT US</span><span>CONTACT</span><span>UPDATES</span></nav>
  </div>
  <div class="hero-copy">
    <h1>WELCOME TO<strong>BRIGHT VANTA®</strong></h1>
    <p>Bright Vanta® is an award winning software provider for enterprises and authorities. With deep experience in digital administration we can start new projects on short notice, wherever you are.</p>
    <div class="call">Give us a call or send a message</div>
    <span class="btn">READ MORE</span>
  </div>
</header>

<section class="apps">
  <div class="apps-art" role="img" aria-label="Illustration of colourful mobile phones on rising bars"></div>
  <div class="apps-copy">
    <h2>Bright Vanta® <strong>Web &amp; Mobile Apps</strong></h2>
    <p>Located in Sweden we have provided software since 1999. With our experts in areas like web development and mobile app development, we provide first class solutions and project management.</p>
    <div class="actions"><span class="btn">CONTACT US</span><span class="btn-outline">ORDER QUOTE</span></div>
  </div>
</section>

<section class="services">
  <h2 class="section-title">Some of <strong>our services</strong></h2>
  <p class="section-intro">Bright Vanta® provide senior resources in a vast range of areas within system development. Lately most of our work has been within the fields of app and web development.</p>
  <div class="service-grid">
    <div class="service">
      <svg width="36" height="36" viewBox="0 0 36 36"><rect x="3" y="6" width="30" height="22" rx="2" fill="none" stroke="#1e9bef" stroke-width="2"/><line x1="3" y1="12" x2="33" y2="12" stroke="#1e9bef" stroke-width="2"/></svg>
      <div><h3>Web development</h3><p>We provide skilled, enthusiastic experts to boost your team, from a single page to large multi-site platforms.</p></div>
    </div>
    <div class="service">
      <svg width="36" height="36" viewBox="0 0 36 36"><circle cx="18" cy="18" r="14" fill="none" stroke="#1e9bef" stroke-width="2"/><path d="M11 18l5 5 9-10" fill="none" stroke="#1e9bef" stroke-width="2"/></svg>
      <div><h3>Post-Launch Support</h3><p>We offer maintenance and support after launch, keeping your product stable, secure and up to date.</p></div>
    </div>
    <div class="service">
      <svg width="36" height="36" viewBox="0 0 36 36"><path d="M8 28L26 10l4 4-18 18H8z" fill="none" stroke="#1e9bef" stroke-width="2"/></svg>
      <div><h3>Design and UX</h3><p>Our in-house designers create user interfaces that are clear, accessible and built around your users.</p></div>
    </div>
    <div class="service">
      <svg width="36" height="36" viewBox="0 0 36 36"><rect x="10" y="3" width="16" height="30" rx="3" fill="none" stroke="#1e9bef" stroke-width="2"/><circle cx="18" cy="28" r="1.5" fill="#1e9bef"/></svg>
      <div><h3>App development</h3><p>From design to deployment we build native and hybrid apps for every common mobile platform.</p></div>
    </div>
    <div class="service">
      <svg width="36" height="36" viewBox="0 0 36 36"><rect x="4" y="4" width="28" height="28" rx="3" fill="none" stroke="#1e9bef" stroke-width="2"/><line x1="4" y1="14" x2="32" y2="14" stroke="#1e9bef" stroke-width="2"/><line x1="14" y1="14" x2="14" y2="32" stroke="#1e9bef" stroke-width="2"/></svg>
      <div><h3>Quillpage CMS</h3><p>A flexible content platform that lets editors update their sites quickly and safely.</p></div>
    </div>
  </div>
</section>

<section class="clients">
  <div class="clients-inner">
    <h2 class="section-title">Some of <strong>our clients</strong></h2>
    <span class="view-all">VIEW ALL ›</span>
    <div class="client-grid">
      <div class="client-card">
        <div class="client-name"><span class="client-dot"></span>Fieldhold Growers</div>
        <p>A members organisation for farmers. We built a booking and administration system that handles applications for the whole country.</p>
        <div class="client-link">Service App for farming equipment</div>
        <div class="client-sub">Fieldhold Growers</div>
      </div>
      <div class="client-card">
        <div class="client-name"><span class="client-dot"></span>Culturebay</div>
        <p>A municipal culture office. We delivered a ticket system for events and exhibitions, linked to existing administrative tools.</p>
        <div class="client-link">Ticket booking app</div>
        <div class="client-sub">Culturebay</div>
      </div>
      <div class="client-card">
        <div class="client-name"><span class="client-dot"></span>Tallyfair</div>
        <p>An event organiser with large yearly fairs. We created a marketing platform with registration, payments and exhibitor tools.</p>
        <div class="client-link">Event Marketing Portal</div>
        <div class="client-sub">Tallyfair</div>
      </div>
    </div>
  </div>
</section>

<section class="quote">
  <div class="quote-copy">
    <h2>Bright Vanta®<strong>Request for a quote</strong></h2>
    <p>Start the exciting journey of creating a mobile app or website by submitting a request for a quote. Requests are handled quickly and with integrity.</p>
    <span class="btn">REQUEST QUOTE</span>
  </div>
  <div class="devices-art" role="img" aria-label="Illustration of a desktop, laptop, tablet and phone showing a website"></div>
</section>

<footer class="footer">
  <div class="footer-panel">
    <div class="footer-brand"><span class="brand-mark"></span>BRIGHT VANTA</div>
    <div>
      <h4>WANT TO BE UPDATED ABOUT BRIGHT VANTA?</h4>
      <div class="field"></div>
      <div class="field"></div>
      <span class="btn btn-dark">SUBSCRIBE</span>
    </div>
    <div>
      <h4>QUICK LINKS</h4>
      <div class="small">Services<br>Projects<br>About us<br>Updates<br>Contact</div>
    </div>
    <div>
      <h4>CALL US</h4>
      <div class="contact-row">
        <svg width="14" height="14" viewBox="0 0 14 14"><path d="M3 1l2 3-1.5 1.5a8 8 0 005 5L10 9l3 2-1 2C6 13 1 8 1 2z" fill="#fff"/></svg>
        +46 (0)10 555 01 20
      </div>
      <div class="contact-row">
        <svg width="14" height="14" viewBox="0 0 14 14"><rect x="1" y="3" width="12" height="8" fill="none" stroke="#fff"/><path d="M1 3l6 5 6-5" fill="none" stroke="#fff"/></svg>
        hello@brightvanta.eu
      </div>
      <div class="contact-row">
        <svg width="14" height="14" viewBox="0 0 14 14"><path d="M7 1a4 4 0 014 4c0 3-4 8-4 8S3 8 3 5a4 4 0 014-4z" fill="#fff"/></svg>
        Storgatan 12, Stockholm
      </div>
      <div class="socials"><span></span><span></span><span></span><span></span></div>
    </div>
  </div>
</footer>

</body>
</html>
```